Business Card for Technology Startup

Design a 2-sided business card using the logo provided. We are a digital healthcare platform that provides a mobile app and web UI that helps caregivers, families, and doctors share information and provide better patient outcomes. We use AI and machine learning to help guide patients through their day-to-day life. The final design should communicate stability, peace, comfort, but also align with the image of an AI-driven technology startup.

I'd like the deliverable to by a Photoshop PSD file (with layers) that I can work with in pixlr.com. Should contain the following editable layers:
Name (ex. John Doe)
Title (ex. Founder / CEO)
Email (ex. info@brenvaxa.ai)
Phone (ex. (555) 014-2368)
Website (ex. https://brenvaxa.ai)

```html
<!DOCTYPE html>
<html lang="en">
<head>
<meta charset="utf-8">
<title>Brenvaxa Business Card</title>
<link href="https://fonts.googleapis.com/css2?family=Poppins:wght@300;400;600;700&display=swap" rel="stylesheet">
<style>
  :root {
    --stage: #969696;
    --card-dark: #232323;
    --card-dark-deep: #0e0e0e;
    --card-light: #ffffff;
    --accent: #18b6e4;
    --ink: #111111;
    --ink-muted: #595959;
    --ink-soft: #6d6d6d;
    --white: #ffffff;
  }
  * { margin: 0; padding: 0; box-sizing: border-box; }
  html, body {
    width: 1200px;
    height: 1000px;
    overflow: hidden;
    background: var(--stage);
    font-family: "Poppins", sans-serif;
  }
  .card {
    position: absolute;
    left: 248px;
    width: 693px;
    height: 399px;
    border-radius: 24px;
    overflow: hidden;
  }
  .card--front { top: 71px; background: var(--card-dark); }
  .card--back { top: 547px; background: var(--card-light); }

  .front-pattern {
    position: absolute;
    inset: 0;
    background: linear-gradient(100deg, var(--card-dark-deep) 0%, var(--card-dark) 55%, #2c2c2c 100%);
  }

  .brand {
    position: absolute;
    display: flex;
    align-items: center;
    gap: 10px;
    transform: translate(-50%, -50%);
    font-weight: 600;
    font-size: 36px;
    letter-spacing: 0.5px;
    line-height: 1;
    white-space: nowrap;
  }
  .brand__dot {
    width: 12px;
    height: 12px;
    border-radius: 50%;
    background: var(--accent);
  }
  .brand--front { left: 522px; top: 323px; color: var(--white); }
  .brand--back { left: 504px; top: 98px; color: var(--ink); }

  .back-decor {
    position: absolute;
    left: 0;
    top: 0;
    width: 240px;
    height: 399px;
    background: radial-gradient(circle at 30% 55%, #eef8fb 0%, rgba(255,255,255,0) 70%);
  }

  .contact {
    position: absolute;
    left: 504px;
    transform: translateX(-50%);
    text-align: center;
    white-space: nowrap;
  }
  .contact__name {
    top: 156px;
    color: var(--accent);
    font-weight: 700;
    font-size: 27px;
    line-height: 34px;
  }
  .contact__title {
    top: 185px;
    color: var(--ink-muted);
    font-weight: 400;
    font-size: 15px;
    line-height: 20px;
  }
  .contact__icons {
    top: 215px;
    display: flex;
    gap: 5px;
  }
  .contact__icons svg { width: 24px; height: 24px; }
  .contact__email, .contact__phone {
    color: var(--ink-soft);
    font-weight: 300;
    font-size: 19px;
    line-height: 24px;
  }
  .contact__email { top: 249px; }
  .contact__phone { top: 276px; }
  .contact__web {
    top: 329px;
    font-size: 20px;
    line-height: 26px;
    color: var(--ink-muted);
    font-weight: 400;
  }
  .contact__web-name { color: var(--accent); font-weight: 600; }
</style>
</head>
<body>
  <section class="card card--front">
    <div class="front-pattern" role="img" aria-label="Dark background with a repeating pattern of small molecular symbols fading from left to right"></div>
    <div class="brand brand--front"><span class="brand__dot"></span><span>brenvaxa</span></div>
  </section>

  <section class="card card--back">
    <div class="back-decor" role="img" aria-label="Faint large outline decoration in pale blue"></div>
    <div class="brand brand--back"><span class="brand__dot"></span><span>brenvaxa</span></div>

    <p class="contact contact__name">JOHN DOE</p>
    <p class="contact contact__title">FOUNDER / CEO</p>
    <div class="contact contact__icons">
      <svg viewBox="0 0 24 24" aria-label="Phone">
        <circle cx="12" cy="12" r="11" fill="none" stroke="var(--accent)" stroke-width="1"/>
        <path d="M8.5 6.5 L10 6 L11 8.5 L10 9.5 Q10.8 12.5 14 14 L15 13 L17.5 14 L17 15.5 Q15.5 17.5 12.5 16 Q8 13.5 7 9.5 Q6.8 7.5 8.5 6.5 Z" fill="none" stroke="var(--accent)" stroke-width="0.9" stroke-linejoin="round"/>
      </svg>
      <svg viewBox="0 0 24 24" aria-label="Email">
        <circle cx="12" cy="12" r="11" fill="none" stroke="var(--accent)" stroke-width="1"/>
        <rect x="6.5" y="8.5" width="11" height="7.5" fill="none" stroke="var(--accent)" stroke-width="0.9"/>
        <path d="M6.5 8.5 L12 13 L17.5 8.5 M6.5 16 L10.5 12 M17.5 16 L13.5 12" fill="none" stroke="var(--accent)" stroke-width="0.9"/>
      </svg>
    </div>
    <p class="contact contact__email">info@brenvaxa.ai</p>
    <p class="contact contact__phone">(555) 014-2368</p>
    <p class="contact contact__web"><span class="contact__web-name">brenvaxa</span>.ai</p>
  </section>
</body>
</html>
```